Velis Tarn

We are an online company, specialising in Relationship enhancement & sexual health. Empowering couples & singles to learn more about their bodies & enhance their sex lives.

We are looking to create a flyer to hand to customers & mail out. We want to peak their interest to bring them to our website.

I want to stress that we want a professional, elegant message, keeping away from the usual innuendos of adult stores.

Something suggestive, but not corny.

Visit our Website www.velistarn.com.au to get a feel of our business.

Target Market(s)

Women 16+
Couples of all ages

Industry/Entity Type

It Company

Font styles to use
Serif

Requirements
Must have
• Logo
• Website URL - www.velistarn.com.au
• Logo of Facebook, instagram
• Our slogan 'Elevate your life'
Nice to have
• Discount offered
Should not have
• Sleezy
• No nudity

```html
<!DOCTYPE html>
<html lang="en">
<head>
<meta charset="utf-8">
<title>Velis Tarn – Elevate Your Life</title>
<link rel="stylesheet" href="https://fonts.googleapis.com/css2?family=Lato:wght@300;400;700&family=Raleway:wght@200;300&display=swap">
<style>
  :root {
    --red: #d0202b;
    --red-dark: #a5131c;
    --ink: #4a4a4a;
    --ink-soft: #6d6d6d;
    --paper: #ffffff;
    --mist: #eef0f2;
  }
  * { margin: 0; padding: 0; box-sizing: border-box; }
  html, body { width: 849px; height: 1200px; overflow: hidden; background: var(--paper); }
  .flyer {
    position: relative;
    width: 849px;
    height: 1200px;
    overflow: hidden;
    background: var(--paper);
    font-family: "Lato", Arial, sans-serif;
    color: var(--ink);
  }
  .wave { position: absolute; left: 0; width: 849px; }
  .wave--top { top: 0; height: 110px; }
  .wave--bottom { bottom: 0; height: 90px; }

  .brand {
    position: absolute;
    top: 52px;
    left: 56px;
    display: flex;
    align-items: center;
    gap: 14px;
  }
  .brand__dot {
    width: 42px; height: 42px;
    border-radius: 50%;
    background: var(--red);
  }
  .brand__name {
    font-family: "Lato", Arial, sans-serif;
    font-weight: 700;
    font-size: 44px;
    color: var(--red);
    letter-spacing: 0.5px;
  }

  .photo {
    position: absolute;
    top: 230px;
    left: 0;
    width: 849px;
    height: 720px;
    background:
      radial-gradient(ellipse 60% 45% at 45% 55%, #e6c6b0 0%, rgba(230,198,176,0) 70%),
      radial-gradient(ellipse 30% 25% at 70% 48%, #8a6a55 0%, rgba(138,106,85,0) 70%),
      linear-gradient(180deg, rgba(255,255,255,0) 0%, #eceef0 25%, #e8eaec 70%, rgba(255,255,255,0) 100%);
  }

  .badge {
    position: absolute;
    top: 110px;
    left: 650px;
    width: 140px;
    height: 190px;
  }
  .badge__text {
    position: absolute;
    top: 32px;
    left: 0;
    width: 140px;
    text-align: center;
    color: var(--paper);
  }
  .badge__value { display: block; font-size: 38px; font-weight: 400; line-height: 1; }
  .badge__label { display: block; font-size: 15px; letter-spacing: 1px; margin-top: 4px; }

  .slogan {
    position: absolute;
    top: 290px;
    left: 0;
    width: 849px;
    text-align: center;
    font-family: "Raleway", Arial, sans-serif;
    color: var(--ink);
    line-height: 0.95;
    text-transform: uppercase;
  }
  .slogan__small { display: block; font-weight: 300; font-size: 74px; letter-spacing: 2px; }
  .slogan__large { display: block; font-weight: 200; font-size: 122px; }

  .connect {
    position: absolute;
    top: 940px;
    left: 56px;
    width: 310px;
  }
  .connect__label {
    font-size: 18px;
    color: var(--ink-soft);
    padding-top: 8px;
    border-top: 2px dotted #b5b5b5;
    width: 160px;
  }
  .connect__icons { display: flex; gap: 12px; margin-top: 10px; }
  .connect__icon { width: 34px; height: 34px; border-radius: 50%; background: var(--red); }
  .connect__url {
    margin-top: 22px;
    padding: 10px 0;
    border-top: 2px dotted #b5b5b5;
    border-bottom: 2px dotted #b5b5b5;
    font-size: 30px;
    font-weight: 300;
    color: var(--ink);
  }

  .prize {
    position: absolute;
    top: 850px;
    left: 555px;
    width: 230px;
    text-align: center;
  }
  .prize__copy {
    font-size: 15px;
    letter-spacing: 0.5px;
    line-height: 1.3;
    color: var(--ink-soft);
    text-transform: uppercase;
    padding-top: 10px;
    border-top: 2px dotted #b5b5b5;
  }
  .prize__amount {
    margin-top: 8px;
    font-size: 46px;
    font-weight: 700;
    color: var(--red);
  }
  .prize__gift {
    position: absolute;
    top: 970px;
    left: 610px;
    width: 160px;
    height: 170px;
    border-radius: 6px;
    background: linear-gradient(180deg, #d62430 0%, #e9e9ea 35%, #d5d6d8 100%);
  }
</style>
</head>
<body>
<main class="flyer">
  <svg class="wave wave--top" viewBox="0 0 849 110" preserveAspectRatio="none" aria-hidden="true">
    <path d="M0 0 H849 V60 C640 20 420 10 0 18 Z" fill="var(--red)"/>
    <path d="M0 18 C420 10 640 20 849 60 V72 C640 34 420 26 0 30 Z" fill="var(--red-dark)" opacity="0.35"/>
  </svg>

  <div class="photo" role="img" aria-label="Photograph of a smiling couple lying together on white sheets"></div>

  <header class="brand">
    <span class="brand__dot"></span>
    <span class="brand__name">Velis Tarn</span>
  </header>

  <div class="badge">
    <svg width="140" height="190" viewBox="0 0 140 190" aria-hidden="true">
      <path d="M70 186 C60 160 20 130 8 100 A68 68 0 1 1 132 100 C120 130 80 160 70 186 Z" fill="var(--red)"/>
      <circle cx="70" cy="70" r="56" fill="none" stroke="#ffffff" stroke-width="2" opacity="0.6"/>
    </svg>
    <div class="badge__text">
      <span class="badge__value">50%</span>
      <span class="badge__label">DISCOUNT</span>
    </div>
  </div>

  <h1 class="slogan">
    <span class="slogan__small">Elevate</span>
    <span class="slogan__large">Your</span>
    <span class="slogan__large">Life</span>
  </h1>

  <section class="prize">
    <p class="prize__copy">Chance to win a mystery<br>gift valued at</p>
    <p class="prize__amount">$150!</p>
  </section>
  <div class="prize__gift" role="img" aria-label="Illustration of a white gift box tied with a red ribbon bow"></div>

  <section class="connect">
    <p class="connect__label">connect with us</p>
    <div class="connect__icons">
      <span class="connect__icon"></span>
      <span class="connect__icon"></span>
      <span class="connect__icon"></span>
    </div>
    <p class="connect__url">www.velistarn.com.au</p>
  </section>

  <svg class="wave wave--bottom" viewBox="0 0 849 90" preserveAspectRatio="none" aria-hidden="true">
    <path d="M0 40 C260 70 560 70 849 10 V90 H0 Z" fill="var(--red)"/>
    <path d="M0 30 C260 60 560 60 849 0 V10 C560 70 260 70 0 40 Z" fill="var(--red-dark)" opacity="0.35"/>
  </svg>
</main>
</body>
</html>
```